Kelvo Auto - help to get me noticed

We not long ago tasked Pixel Harbour to design a logo for my business. I'm happy with the result so would like to have a business card designed as a follow up.

It's an Automotive service and repair business that offers the following -
- Servicing
- General repairs
- Brakes
- Detailing
- Integrity

Kelvo Automotive
Dallin Mereth
0471 926 317

Target Market(s)

Everyday people with the ability to reach out to corporate customers also.

Industry/Entity Type

Automotive

Contact Information for Business Card

Black card, logo, name and phone number on front. Other details on back of card.

```html
<!DOCTYPE html>
<html lang="en">
<head>
<meta charset="utf-8">
<title>Kelvo Automotive – Business Card</title>
<link rel="stylesheet" href="https://fonts.googleapis.com/css2?family=Lato:wght@300;400;700;900&display=swap">
<style>
  :root {
    --backdrop: #2a2a2a;
    --card-black: #000000;
    --green-light: #a4d13f;
    --green-mid: #6cbf45;
    --green-deep: #3d9b45;
    --white: #ffffff;
  }
  * { box-sizing: border-box; margin: 0; padding: 0; }
  html, body {
    width: 1200px;
    height: 970px;
    overflow: hidden;
    background: var(--backdrop);
    font-family: "Lato", sans-serif;
  }
  .sheet {
    width: 1200px;
    height: 970px;
    display: flex;
    flex-direction: column;
    align-items: center;
    justify-content: center;
    gap: 34px;
  }
  .card {
    position: relative;
    width: 760px;
    height: 434px;
    background: var(--card-black);
    overflow: hidden;
  }
  .brand-name {
    position: absolute;
    left: 0;
    right: 0;
    text-align: center;
    font-weight: 900;
    color: var(--green-mid);
    text-transform: uppercase;
    letter-spacing: 2px;
    line-height: 1;
  }

  /* Back of card */
  .card-back .brand-name {
    top: 118px;
    font-size: 60px;
  }
  .service-band {
    position: absolute;
    left: 0;
    right: 0;
    top: 262px;
    height: 46px;
    background: linear-gradient(180deg, var(--green-light) 0%, var(--green-mid) 100%);
    display: flex;
    align-items: center;
    justify-content: center;
  }
  .service-list {
    list-style: none;
    display: flex;
    color: var(--white);
    font-size: 17px;
    font-weight: 400;
    letter-spacing: 1.5px;
    text-transform: uppercase;
  }
  .service-list li + li::before {
    content: "|";
    margin: 0 14px;
  }

  /* Front of card */
  .card-front .brand-name {
    top: 92px;
    font-size: 60px;
  }
  .contact-name {
    position: absolute;
    left: 0;
    right: 0;
    top: 210px;
    text-align: center;
    color: var(--green-deep);
    font-weight: 900;
    font-size: 36px;
    letter-spacing: 1px;
    text-transform: uppercase;
  }
  .contact-phone {
    position: absolute;
    left: 0;
    right: 0;
    top: 262px;
    text-align: center;
    color: var(--white);
    font-weight: 300;
    font-size: 72px;
    letter-spacing: 2px;
  }
  .edge-line {
    position: absolute;
    left: 0;
    right: 0;
    bottom: 0;
    height: 6px;
    background: var(--green-mid);
  }
</style>
</head>
<body>
<main class="sheet">
  <section class="card card-back">
    <p class="brand-name">Kelvo Automotive</p>
    <div class="service-band">
      <ul class="service-list">
        <li>Servicing</li>
        <li>General Repairs</li>
        <li>Brakes</li>
        <li>Detailing</li>
        <li>Integrity</li>
      </ul>
    </div>
  </section>

  <section class="card card-front">
    <p class="brand-name">Kelvo Automotive</p>
    <p class="contact-name">Dallin Mereth</p>
    <p class="contact-phone">0471 926 317</p>
    <div class="edge-line"></div>
  </section>
</main>
</body>
</html>
```